Poster Design to promote Adult Group Guitar Classes for Music School

We're a young music school trying to promote our Adult Group Guitar Beginner 101 classes, and need an eye catching poster design to promote the course. We'll be wanting to put the posters up on telegraph poles, community notice boards, shop front windows, cafes, shops and the around the general area of Sydney's Inner West, plus be able to covert it as a jpg image which we can forward to our mailing list and post on our website.

The poster should be visually appealing and incorporate images of what we are trying to promote.

We'd like the design to be professional, fun, creative and compliment our current logo design and colours.

Be sure to highlight 'Register Now'

Text to be used as follows:

GROUP GUITAR 101 CLASSES
For Beginner Adults

NEWTOWN

8 week Jam Packed Course
Small Groups (max. 6 people)
Guitars provided on site
Weekly hour long classes
Perfect introduction to learning the fundamentals
Materials Included
No music experience required

RESGISTER NOW – Limited Spaces
Visit our website for class times and start dates
www.brightreedstudio.com.au

T: (02) 7413 2958
E: info@brightreedstudio.com.au

PRIVATE MUSIC TUITION | ENSEMBLE | GROUP | GLEE CLUB

Industry/Entity Type

School

Requirements
Must have
• Bright Reed Studio Logo

A3 poster size

Be in a print ready file for off-set printing. CMYK with 3mm bleed

```html
<!DOCTYPE html>
<html lang="en">
<head>
<meta charset="utf-8">
<title>Group Guitar 101 Classes — Bright Reed Studio</title>
<link rel="stylesheet" href="https://fonts.googleapis.com/css2?family=Arvo:wght@400;700&family=Kalam:wght@400&family=Crimson+Text:wght@400;700&display=swap">
<style>
  :root {
    --page: #ffffff;
    --paper: #fbfaf8;
    --frame: #3a3a3a;
    --orange: #e8581c;
    --orange-deep: #c9460f;
    --amber: #f6a623;
    --gold: #f7c948;
    --ink: #1d1d1d;
    --teal: #2aa5b5;
    --wood-dark: #4a2410;
    --wood-mid: #9a5325;
    --wood-light: #e0a45a;
  }
  * { box-sizing: border-box; margin: 0; padding: 0; }
  html, body { width: 1200px; height: 900px; overflow: hidden; background: var(--page); }

  .poster {
    position: absolute; left: 297px; top: 21px;
    width: 607px; height: 853px;
    background: var(--paper);
    border: 1px solid var(--frame);
    overflow: hidden;
  }

  .hero-visual {
    position: absolute; left: 250px; top: 0; width: 357px; height: 853px;
    background:
      radial-gradient(ellipse 55% 28% at 70% 14%, rgba(247,201,72,0.75), rgba(246,166,35,0.25) 60%, rgba(255,255,255,0) 100%),
      radial-gradient(ellipse 48% 30% at 52% 66%, var(--wood-light), var(--wood-mid) 45%, var(--wood-dark) 80%, rgba(74,36,16,0) 100%),
      linear-gradient(180deg, rgba(255,255,255,0) 0%, rgba(240,235,228,0.6) 100%);
  }

  .headline {
    position: absolute; left: 30px; top: 58px;
    font-family: "Arvo", serif; font-weight: 700;
    font-size: 48px; line-height: 60px;
    color: var(--orange); letter-spacing: 0.5px;
  }

  .audience {
    position: absolute; left: 30px; top: 226px;
    font-family: "Arvo", serif; font-weight: 700;
    font-size: 29px; line-height: 38px;
    color: var(--orange);
  }

  .features {
    position: absolute; left: 26px; top: 326px;
    list-style: none;
    font-family: "Kalam", cursive;
    font-size: 18px; line-height: 19px;
    color: var(--ink);
  }
  .features li { padding-left: 16px; position: relative; }
  .features li::before { content: "♪"; position: absolute; left: 0; top: 0; }

  .register {
    position: absolute; left: 21px; top: 543px;
    width: 234px; height: 45px;
  }
  .register svg { position: absolute; inset: 0; }
  .register-label {
    position: absolute; left: 0; right: 12px; top: 4px;
    text-align: center;
    font-family: "Arvo", serif; font-weight: 700;
    font-size: 19px; line-height: 22px; color: #fff;
  }
  .register-note {
    position: absolute; left: 0; right: 12px; top: 27px;
    text-align: center;
    font-family: "Arvo", serif; font-weight: 700;
    font-size: 9px; color: #fff;
  }

  .brand {
    position: absolute; left: 45px; top: 660px;
    display: flex; align-items: center; gap: 8px;
  }
  .brand-dot { width: 22px; height: 22px; border-radius: 50%; background: var(--orange); }
  .brand-name {
    font-family: "Arvo", serif; font-weight: 700;
    font-size: 18px; color: var(--teal);
  }

  .contact {
    position: absolute; left: 21px; top: 771px;
    font-family: "Crimson Text", serif;
    font-size: 10px; line-height: 12px; color: var(--ink);
  }
  .contact strong { font-weight: 700; }

  .services {
    position: absolute; left: 21px; top: 828px;
    font-family: "Crimson Text", serif; font-weight: 700;
    font-size: 9.5px; letter-spacing: 0.3px; color: var(--ink);
  }
</style>
</head>
<body>
  <main class="poster">
    <div class="hero-visual" role="img" aria-label="Sunburst acoustic guitar standing upright against soft golden swirls"></div>

    <h1 class="headline">GROUP GUITAR<br>101 CLASSES</h1>

    <h2 class="audience">For Beginner Adults<br>NEWTOWN</h2>

    <ul class="features">
      <li>8 week Jam Packed Course</li>
      <li>Small Groups (max. 6 people)</li>
      <li>Guitars provided on site</li>
      <li>Weekly hour long classes</li>
      <li>Perfect introduction to<br>learning the fundamentals</li>
      <li>Materials Included</li>
      <li>No music experience required</li>
    </ul>

    <div class="register">
      <svg width="234" height="45" viewBox="0 0 234 45" aria-hidden="true">
        <defs>
          <linearGradient id="ribbon-fill" x1="0" y1="0" x2="0" y2="1">
            <stop offset="0" stop-color="#f9b233"/>
            <stop offset="1" stop-color="#ee7d1a"/>
          </linearGradient>
        </defs>
        <polygon points="0,2 222,2 234,22 222,43 0,43" fill="url(#ribbon-fill)"/>
        <polygon points="0,2 222,2 226,8 0,8" fill="#fcd27a" opacity="0.6"/>
      </svg>
      <div class="register-label">RESGISTER NOW</div>
      <div class="register-note">Limited Spaces</div>
    </div>

    <div class="brand">
      <span class="brand-dot"></span>
      <span class="brand-name">Bright Reed Studio</span>
    </div>

    <p class="contact">
      Visit our website for class times and start dates:<br>
      <strong>www.brightreedstudio.com.au</strong><br>
      <strong>T: (02) 7413 2958</strong><br>
      <strong>E: info@brightreedstudio.com.au</strong>
    </p>

    <p class="services">PRIVATE MUSIC TUITION | ENSEMBLE | GROUP | GLEE CLUB</p>
  </main>
</body>
</html>
```